Business Card Design for general contractor or developer

General Contractors. We build new buildings as well as redesign and/or remodel existing buildings. Mostly residential, but we want to expand to commercial as well, so we want the design not to be residential specific.We want the design to be modern, but necessarily minimalistic. A monogram type is also a consideration, but would like to see all ideas.

Target Market(s)

Real estate investors, homeowners, future homeowners, commercial building owners

Industry/Entity Type

Contractor

Contact Information for Business Card

BRIMCOVE Developers Corp, 2917 NE 88th Avenue Suite 412 Coral Springs, FL 33071, Darren Kopec, (305) 555-0148, darren@brimcovedev.example

Font styles to use
Other font styles liked:
• Modern type font

Requirements
Must have
• Must be modern looking
Nice to have
• Metallic type or a standout feature
Should not have
• Tools, floorplans

```html
<!DOCTYPE html>
<html lang="en">
<head>
<meta charset="utf-8">
<title>BRIMCOVE Developers Corp – Business Card</title>
<link rel="stylesheet" href="https://fonts.googleapis.com/css2?family=Oswald:wght@400;500&display=swap">
<style>
  :root {
    --backdrop: #141414;
    --card-black: #0d0d0d;
    --card-black-soft: #1c1c1c;
    --silver: #cfcfcf;
    --silver-dim: #9a9a9a;
    --rule: #6e6e6e;
  }
  * { box-sizing: border-box; margin: 0; padding: 0; }
  html, body {
    width: 1200px; height: 871px; overflow: hidden;
    background: var(--backdrop);
    font-family: "Oswald", sans-serif;
  }
  .canvas {
    position: relative; width: 1200px; height: 871px;
    display: flex; flex-direction: column; align-items: center; justify-content: center; gap: 44px;
  }
  .card {
    position: relative; width: 610px; height: 349px;
    background: linear-gradient(135deg, var(--card-black-soft), var(--card-black) 60%);
    box-shadow: 0 18px 40px rgba(0,0,0,.6);
    color: var(--silver);
  }

  /* Back side: brand */
  .card--back {
    display: flex; flex-direction: column; align-items: center; justify-content: center; gap: 14px;
    background: linear-gradient(120deg, #3a3a3a 0%, #1a1a1a 35%, var(--card-black) 70%);
  }
  .brand-lockup { display: flex; align-items: center; gap: 18px; }
  .brand-circle {
    width: 64px; height: 64px; border-radius: 50%;
    border: 4px solid var(--silver);
  }
  .brand-name {
    font-size: 52px; font-weight: 500; letter-spacing: 10px; color: var(--silver);
  }
  .brand-tagline {
    font-size: 20px; font-weight: 400; letter-spacing: 8px; color: var(--silver-dim);
    text-transform: uppercase;
  }

  /* Front side: contact */
  .card--front { display: flex; align-items: center; padding: 0 36px; }
  .front-brand {
    width: 210px; display: flex; align-items: center; justify-content: center; gap: 10px;
  }
  .front-brand .brand-circle { width: 30px; height: 30px; border-width: 3px; }
  .front-brand .brand-name { font-size: 26px; letter-spacing: 3px; }
  .divider { width: 1px; height: 190px; background: var(--rule); margin: 0 30px 0 16px; }
  .contact { display: flex; flex-direction: column; gap: 8px; }
  .contact-name { font-size: 34px; font-weight: 500; letter-spacing: 2px; color: var(--silver); margin-bottom: 4px; }
  .contact-row { display: flex; align-items: flex-start; gap: 12px; font-size: 17px; letter-spacing: 1px; line-height: 1.3; }
  .contact-icon { width: 16px; height: 16px; flex: none; margin-top: 4px; fill: var(--silver-dim); }
</style>
</head>
<body>
<main class="canvas">

  <section class="card card--back" aria-label="Card back">
    <div class="brand-lockup">
      <span class="brand-circle"></span>
      <span class="brand-name">BRIMCOVE</span>
    </div>
    <p class="brand-tagline">Developers Corp</p>
  </section>

  <section class="card card--front" aria-label="Card front">
    <div class="front-brand">
      <span class="brand-circle"></span>
      <span class="brand-name">BRIMCOVE</span>
    </div>
    <div class="divider"></div>
    <div class="contact">
      <h1 class="contact-name">Darren Kopec</h1>
      <div class="contact-row">
        <svg class="contact-icon" viewBox="0 0 16 16" aria-hidden="true"><path d="M8 0a5.5 5.5 0 0 0-5.5 5.5C2.5 9.6 8 16 8 16s5.5-6.4 5.5-10.5A5.5 5.5 0 0 0 8 0zm0 7.8a2.3 2.3 0 1 1 0-4.6 2.3 2.3 0 0 1 0 4.6z"/></svg>
        <span>2917 NE 88th Avenue<br>Suite 412 Coral Springs FL 33071</span>
      </div>
      <div class="contact-row">
        <svg class="contact-icon" viewBox="0 0 16 16" aria-hidden="true"><path d="M3.6 1 6 3.8 4.7 5.6a9.5 9.5 0 0 0 5.7 5.7l1.8-1.3L15 12.4 13.4 15C6.9 14.6 1.4 9.1 1 2.6z"/></svg>
        <span>(305) 555-0148</span>
      </div>
      <div class="contact-row">
        <svg class="contact-icon" viewBox="0 0 16 16" aria-hidden="true"><path d="M1 3h14v10H1zm1.2 1.2v.3L8 8.6l5.8-4.1v-.3zM2.2 6v5.8h11.6V6L8 10.1z"/></svg>
        <span>darren@brimcovedev.example</span>
      </div>
    </div>
  </section>

</main>
</body>
</html>
```